Business Card Design for Event Planning Company

Create a business card for event planning company using our new logo. After I pick the design, I will need files made for 6 employees. Our company provides event design & logistics services as well as venue management. The font should be sans serif and complementary to the logo. I will need to know the name of the font selected for the final design. The phone numbers listed should be separated by "." not "-"

Address for the card
PO Box 218, Washington, DC 20019

Card One
Lorna Pettigrew
lpettigrew@galaplanora.com
202.481.7032

Card Two
Marisol Dunleavy
mdunleavy@galaplanora.com
202.416.2950

Card Three
Rebecca Vasquetti
rvasquetti@galaplanora.com
978.527.6043

Card Four
Tessa Brink
tbrink@galaplanora.com
202.458.1276

Card Five
Ada-Rose Pemberton-Nwaku
adarose@galaplanora.com
202.819.3047

Card Six
Valerie Thornbury
Valerie@galaplanora.com
202.592.8134

Target Market(s)

Corporate/Non-Profit

Industry/Entity Type

Event Planning

Contact Information for Business Card

Address for the card

Card One
Lorna Pettigrew
lpettigrew@galaplanora.com
202.481.7032

Card Two
Marisol Dunleavy
202.416.2950

Card Three
Rebecca Vasquetti
978.527.6043

Card Four
Tessa Brink
tbrink@galaplanora.com
202.458.1276

Card Five
Ada-Rose Pemberton-Nwaku
202.819.3047

Card Six
Valerie Thornbury
202.592.8134

Font styles to use
Sans Serif

Colors

Designer to choose colors to be used in the design.

Requirements
Must have
• Two-sided with logo
Should not have
• Extra colors or be too busy

```html
<!DOCTYPE html>
<html lang="en">
<head>
<meta charset="utf-8">
<title>Galaplanora Business Card</title>
<link rel="stylesheet" href="https://fonts.googleapis.com/css2?family=Questrial&display=swap">
<style>
  :root {
    --stage: #d9d5d1;
    --card: #1c1c1d;
    --card-edge: #262627;
    --teal: #5fb3b0;
    --ink-light: #e6e6e6;
    --ink-soft: #c9c9c9;
    --mark-grey: #3c3c3e;
  }
  * { box-sizing: border-box; margin: 0; padding: 0; }
  html, body {
    width: 1200px;
    height: 715px;
    overflow: hidden;
    background: var(--stage);
    font-family: "Questrial", sans-serif;
  }
  .sheet {
    position: relative;
    width: 1200px;
    height: 715px;
    display: flex;
    align-items: center;
    justify-content: center;
    gap: 40px;
  }
  .card {
    position: relative;
    width: 540px;
    height: 309px;
    background: var(--card);
    border: 1px solid var(--card-edge);
    border-radius: 3px;
    overflow: hidden;
  }

  /* Back side */
  .card-back .brand-mark {
    position: absolute;
    left: 0; right: 0;
    top: 92px;
    text-align: center;
    font-size: 64px;
    letter-spacing: 1px;
    color: var(--mark-grey);
  }
  .card-back .web-line {
    position: absolute;
    left: 0; right: 0;
    bottom: 52px;
    display: flex;
    align-items: center;
    justify-content: center;
    gap: 16px;
    font-size: 15px;
    letter-spacing: 0.5px;
    color: var(--ink-soft);
  }
  .card-back .rule {
    width: 96px;
    height: 1px;
    background: var(--teal);
  }

  /* Front side */
  .card-front .brand {
    position: absolute;
    left: 34px;
    top: 112px;
    display: flex;
    flex-direction: column;
    align-items: center;
    gap: 8px;
  }
  .card-front .brand-dot {
    width: 22px;
    height: 22px;
    border-radius: 50%;
    background: var(--teal);
  }
  .card-front .brand-name {
    font-size: 31px;
    color: var(--teal);
    letter-spacing: 0.3px;
  }
  .card-front .contact {
    position: absolute;
    left: 292px;
    top: 148px;
    color: var(--ink-light);
    font-size: 13.5px;
    line-height: 1.45;
  }
  .card-front .person-name {
    font-size: 19px;
    color: var(--teal);
    margin-bottom: 8px;
    letter-spacing: 0.3px;
  }
  .card-front .contact-row {
    display: flex;
    align-items: center;
    gap: 8px;
  }
  .card-front .contact-row svg { flex: none; }
  .card-front .address { margin-top: 1px; }
</style>
</head>
<body>
<main class="sheet">
  <section class="card card-back" aria-label="Card back">
    <div class="brand-mark">galaplanora</div>
    <div class="web-line">
      <span class="rule"></span>
      <span class="website">www.galaplanora.com</span>
      <span class="rule"></span>
    </div>
  </section>

  <section class="card card-front" aria-label="Card front">
    <div class="brand">
      <span class="brand-dot"></span>
      <span class="brand-name">galaplanora</span>
    </div>
    <div class="contact">
      <div class="person-name">Valerie Thornbury</div>
      <div class="contact-row">
        <svg width="11" height="11" viewBox="0 0 24 24" aria-hidden="true">
          <path fill="#9a9a9a" d="M6.6 10.8a15.1 15.1 0 0 0 6.6 6.6l2.2-2.2a1 1 0 0 1 1-.25 11.4 11.4 0 0 0 3.6.57 1 1 0 0 1 1 1V20a1 1 0 0 1-1 1A17 17 0 0 1 3 4a1 1 0 0 1 1-1h3.5a1 1 0 0 1 1 1c0 1.25.2 2.45.57 3.57a1 1 0 0 1-.25 1z"/>
        </svg>
        <span>202.592.8134</span>
      </div>
      <div class="contact-row">
        <svg width="11" height="11" viewBox="0 0 24 24" aria-hidden="true">
          <rect x="2" y="5" width="20" height="14" rx="1.5" fill="#9a9a9a"/>
          <path d="M3 6l9 7 9-7" fill="none" stroke="#1c1c1d" stroke-width="1.8"/>
        </svg>
        <span>Valerie@galaplanora.com</span>
      </div>
      <div class="address">PO Box 218, Washington, DC 20019</div>
    </div>
  </section>
</main>
</body>
</html>
```